Real Estate Seller Financing Postcard

I need a postcard that lays out these options contained in the notes that grabs attention, explains the two options easily and is eye-catching. The front needs to have the percentages on it and information about it and on the other side One side exact Text is:
"Monthly income without tenant headaches" in big letters. Also on front "Get
110%
add an "or"
160% of market value for your property. ". The percentages should be displayed and that is not to be a sentence of text. Other side text: I need bullets points for these "Formal protection as a lien holder against home
No commission or closing cost
Fast closings possible
Property taken as is so no repairs.

Add to the top of the back in "It’s simple. I am a new investor without down payment capital who still want to double our portfolio this year to grow our portfolio."
Here are the two options that are to be the largest part of the back
Option 1, you can receive 80% now cash and 30% over a short period of time including interest.

Option 2, where act like a bank allowing you to make 150% if you finance the whole property(ies). No gimmicks and surprises, just simple unconventional financing.

Include Logo Somewhere

Target Market(s)

Property Owners Wanting to Sell Their Property

Industry/Entity Type

Real Estate Investing

Requirements
Must have
• The options promiment and each side with its respective information. Must have logo somewhere
Nice to have
• The options in color other than black.
Should not have
• A picture of money on the front. Any other image is okay.

```html
<!DOCTYPE html>
<html lang="en">
<head>
<meta charset="utf-8">
<title>Meridian Real Estate Group – Seller Financing Postcard</title>
<link rel="stylesheet" href="https://fonts.googleapis.com/css2?family=Montserrat:ital,wght@0,400;0,500;0,600;0,700;0,800;1,500&display=swap">
<style>
  :root {
    --navy: #12428f;
    --navy-deep: #0d3474;
    --green: #139a3f;
    --ink: #1f1f22;
    --paper: #ffffff;
    --mist: #e9eaee;
    --box: #e3e4e8;
    --text-dark: #2b2b33;
    --backdrop: #cfd2d8;
    --rule: #b9bcc4;
  }
  * { margin: 0; padding: 0; box-sizing: border-box; }
  html, body { width: 1200px; height: 1000px; overflow: hidden; }
  body { background: var(--backdrop); font-family: "Montserrat", sans-serif; position: relative; }

  .postcard { position: absolute; left: 250px; width: 700px; height: 470px; background: var(--paper);
    overflow: hidden; box-shadow: 0 6px 18px rgba(0,0,0,.18); }
  .postcard--front { top: 20px; }
  .postcard--back { top: 510px; }
  .postcard svg.shapes { position: absolute; inset: 0; }
  .abs { position: absolute; }

  /* front */
  .headline { left: 34px; top: 40px; color: var(--paper); text-transform: uppercase; line-height: 1; }
  .headline__top { font-size: 28px; font-weight: 500; letter-spacing: .5px; }
  .headline__big { font-size: 60px; font-weight: 500; letter-spacing: 1px; margin: 8px 0 6px; }
  .headline__bottom { font-size: 28px; font-weight: 500; letter-spacing: .5px; }

  .offer { left: 34px; top: 216px; color: var(--paper); }
  .offer__row { display: flex; align-items: baseline; gap: 12px; }
  .offer__get { background: var(--paper); color: var(--text-dark); font-size: 18px; font-weight: 500;
    padding: 4px 26px 4px 40px; border-radius: 0 16px 16px 0; margin-left: -34px; }
  .offer__pct { font-size: 40px; font-weight: 800; }
  .offer__or { font-size: 18px; font-weight: 700; }
  .offer__note { font-size: 12px; font-weight: 500; text-transform: uppercase; margin-top: 4px; letter-spacing: .3px; }

  .photo-front { left: 375px; top: 20px; width: 290px; height: 290px; border-radius: 50%;
    border: 9px solid var(--paper); background: radial-gradient(circle at 50% 45%, #c9b18e, #6f8fb4 70%, #d9dbe0);
    box-shadow: 0 4px 14px rgba(0,0,0,.2); }

  .benefits { left: 40px; top: 315px; }
  .benefits__title { color: var(--navy); font-size: 14px; font-weight: 700; text-transform: uppercase; line-height: 1.2; }
  .benefits__list { list-style: none; margin-top: 8px; }
  .benefits__list li { display: flex; align-items: center; gap: 8px; font-size: 11px; font-weight: 500;
    color: var(--text-dark); text-transform: uppercase; margin-bottom: 5px; }
  .benefits__icon { width: 20px; height: 20px; border-radius: 50%; border: 1.5px solid var(--green);
    display: flex; align-items: center; justify-content: center; }

  .brand { display: flex; align-items: center; gap: 10px; }
  .brand__mark { width: 44px; height: 44px; border-radius: 50%; border: 2.5px solid var(--navy); }
  .brand__rule { width: 1px; height: 40px; background: var(--navy); }
  .brand__name { color: var(--navy); font-weight: 700; line-height: 1; text-transform: uppercase; }
  .brand__name span { display: block; font-size: 11px; margin-top: 4px; letter-spacing: .5px; }
  .postcard--front .brand { right: 26px; bottom: 62px; }
  .postcard--front .brand__name { font-size: 26px; }

  .contact-bar { display: flex; gap: 22px; color: var(--paper); font-size: 11px; font-weight: 500; white-space: nowrap; }
  .contact-bar__item { display: flex; align-items: center; gap: 6px; }
  .contact-bar__dot { width: 12px; height: 12px; border-radius: 50%; background: var(--green);
    display: flex; align-items: center; justify-content: center; }
  .postcard--front .contact-bar { left: 40px; bottom: 12px; }

  /* back */
  .photo-back { left: 0; top: 0; width: 470px; height: 175px;
    background: linear-gradient(120deg, #8a8f96, #c7c4bd 55%, #9da6b1);
    clip-path: polygon(0 0, 300px 0, 360px 175px, 0 175px); }
  .intro { left: 28px; top: 188px; width: 360px; padding-left: 12px; border-left: 3px solid var(--green);
    color: var(--paper); font-size: 12.5px; font-style: italic; font-weight: 500; line-height: 1.55; }
  .options { left: 26px; top: 270px; display: flex; gap: 14px; }
  .option { width: 186px; height: 134px; background: var(--box); border-radius: 10px; overflow: hidden;
    box-shadow: 0 3px 8px rgba(0,0,0,.15); }
  .option__title { background: var(--navy); color: var(--paper); font-size: 18px; font-weight: 800;
    text-align: center; padding: 5px 0; text-transform: uppercase; border-radius: 10px 10px 0 0; }
  .option__text { font-size: 10px; color: var(--text-dark); text-align: center; line-height: 1.3; padding: 7px 10px; }
  .contact-tab { left: 0; bottom: 34px; background: var(--green); color: var(--paper); font-size: 12px;
    font-weight: 600; text-transform: uppercase; padding: 5px 22px 5px 26px; border-radius: 0 14px 14px 0; }
  .postcard--back .contact-bar { left: 26px; bottom: 11px; font-size: 10px; gap: 14px; }
  .postcard--back .brand { left: 430px; top: 140px; }
  .postcard--back .brand__name { font-size: 22px; }
  .stamp { right: 26px; top: 24px; width: 80px; height: 92px; border: 1px solid var(--rule); }
  .address-line { height: 1px; background: var(--rule); }
</style>
</head>
<body>

<section class="postcard postcard--front" aria-label="Postcard front">
  <svg class="shapes" viewBox="0 0 700 470" aria-hidden="true">
    <polygon points="0,0 700,0 700,140 460,300 0,300" fill="var(--navy)"/>
    <polygon points="0,232 470,232 420,290 0,290" fill="var(--green)"/>
    <polygon points="700,300 700,430 470,430" fill="var(--mist)"/>
    <polygon points="0,430 700,430 700,470 0,470" fill="var(--ink)"/>
  </svg>

  <h1 class="abs headline">
    <div class="headline__top">Monthly income</div>
    <div class="headline__big">Without</div>
    <div class="headline__bottom">Tenant headaches</div>
  </h1>

  <div class="abs offer">
    <div class="offer__row">
      <span class="offer__get">GET</span>
      <span class="offer__pct">110%</span>
      <span class="offer__or">or</span>
      <span class="offer__pct">160%</span>
    </div>
    <div class="offer__note">of market value for your property</div>
  </div>

  <div class="abs photo-front" role="img" aria-label="Photo of a smiling family sitting at home under a cardboard roof, holding a potted plant"></div>

  <div class="abs benefits">
    <h2 class="benefits__title">Formal protection as a lien holder<br>against home:</h2>
    <ul class="benefits__list">
      <li><span class="benefits__icon"><svg width="10" height="10" viewBox="0 0 10 10"><path d="M2 5l2 2 4-4" stroke="var(--green)" stroke-width="1.5" fill="none"/></svg></span>No commission or closing cost</li>
      <li><span class="benefits__icon"><svg width="10" height="10" viewBox="0 0 10 10"><path d="M2 5l2 2 4-4" stroke="var(--green)" stroke-width="1.5" fill="none"/></svg></span>Fast closings possible</li>
      <li><span class="benefits__icon"><svg width="10" height="10" viewBox="0 0 10 10"><path d="M2 5.5L5 2.5 8 5.5M3 5v3h4V5" stroke="var(--green)" stroke-width="1.2" fill="none"/></svg></span>Property taken as is so no repairs</li>
    </ul>
  </div>

  <div class="abs brand">
    <span class="brand__mark"></span>
    <span class="brand__rule"></span>
    <span class="brand__name">Meridian<span>Real Estate Group</span></span>
  </div>

  <div class="abs contact-bar">
    <span class="contact-bar__item"><span class="contact-bar__dot"></span>hello@meridianhomesgroup.com</span>
    <span class="contact-bar__item"><span class="contact-bar__dot"><svg width="7" height="7" viewBox="0 0 10 10"><path d="M2 1l2 2-1 1.5c.8 1.5 1.5 2.2 3 3L7.5 6l2 2-1.5 1.5C5 9 1 5 .5 2z" fill="#fff"/></svg></span>0100 555 0142</span>
    <span class="contact-bar__item"><span class="contact-bar__dot"></span>meridianhomesgroup.com</span>
  </div>
</section>

<section class="postcard postcard--back" aria-label="Postcard back">
  <svg class="shapes" viewBox="0 0 700 470" aria-hidden="true">
    <polygon points="0,175 360,175 388,258 0,264" fill="var(--navy-deep)"/>
    <polygon points="0,430 545,430 560,470 0,470" fill="var(--ink)"/>
  </svg>

  <div class="abs photo-back" role="img" aria-label="Photo of a couple reviewing paperwork and a calculator at a kitchen table"></div>

  <p class="abs intro">It's simple. I am a new investor without down payment capital who still want to double our portfolio this year to grow our portfolio.</p>

  <div class="abs options">
    <article class="option">
      <h3 class="option__title">Option 1</h3>
      <p class="option__text">You can receive 80% now cash and 30% over a short period of time including interest.</p>
    </article>
    <article class="option">
      <h3 class="option__title">Option 2</h3>
      <p class="option__text">Where act like a bank allowing you to make 150% if you finance the whole property(ies). No gimmicks and surprises, just simple unconventional financing.</p>
    </article>
  </div>

  <div class="abs contact-tab">Contact us now</div>
  <div class="abs contact-bar">
    <span class="contact-bar__item"><span class="contact-bar__dot"></span>hello@meridianhomesgroup.com</span>
    <span class="contact-bar__item"><span class="contact-bar__dot"><svg width="7" height="7" viewBox="0 0 10 10"><path d="M2 1l2 2-1 1.5c.8 1.5 1.5 2.2 3 3L7.5 6l2 2-1.5 1.5C5 9 1 5 .5 2z" fill="#fff"/></svg></span>0100 555 0142</span>
    <span class="contact-bar__item"><span class="contact-bar__dot"></span>meridianhomesgroup.com</span>
  </div>

  <div class="abs brand">
    <span class="brand__mark"></span>
    <span class="brand__rule"></span>
    <span class="brand__name">Meridian<span>Real Estate Group</span></span>
  </div>
  <div class="abs stamp"></div>
  <div class="abs address-line" style="left:430px; top:250px; width:245px;"></div>
  <div class="abs address-line" style="left:440px; top:300px; width:235px;"></div>
  <div class="abs address-line" style="left:450px; top:350px; width:225px;"></div>
</section>

</body>
</html>
```